Investment company needing business card

We are wanting a business card which looks sharp and easy on the eye. We are thinking of having a business card with the logo embossed on it, to really make it stand out. We will only have a small amount of information of the business card, person's name, position, email address and phone number

Contact Information for Business Card

Danica Pruett
Executive Assistant
+64 21 547 3162
danicap@harwellcapital.co.nz

Requirements
Must have
• Embossed logo
Should not have
• Not to be busy

```html
<!DOCTYPE html>
<html lang="en">
<head>
<meta charset="utf-8">
<title>Harwell Capital – Business Card</title>
<link rel="stylesheet" href="https://fonts.googleapis.com/css2?family=Roboto:wght@400;500;700;900&display=swap">
<style>
  :root {
    --page-bg: #e6e7e9;
    --card-light-a: #f6f6f6;
    --card-light-b: #dcdddd;
    --card-dark-a: #313234;
    --card-dark-b: #1f2022;
    --brand-green: #1f9e55;
    --ink: #232323;
    --ink-soft: #4a4a4a;
    --band-dark: #3a3b3d;
    --band-rule: #9a9b9d;
    --white: #ffffff;
  }
  * { box-sizing: border-box; margin: 0; padding: 0; }
  html, body { width: 1200px; height: 800px; overflow: hidden; }
  body {
    background: var(--page-bg);
    font-family: "Roboto", Arial, sans-serif;
    position: relative;
  }
  .card {
    position: absolute;
    top: 245px;
    width: 540px;
    height: 310px;
    border-radius: 4px;
    overflow: hidden;
    box-shadow: 0 10px 28px rgba(0,0,0,0.18);
  }
  /* ---------- Front ---------- */
  .card--front {
    left: 40px;
    background: linear-gradient(135deg, var(--card-light-a) 0%, var(--card-light-b) 100%);
  }
  .front__watermark {
    position: absolute;
    right: 24px;
    top: 18px;
    width: 210px;
    height: 200px;
    border-radius: 40px;
    background: linear-gradient(135deg, rgba(0,0,0,0.03), rgba(0,0,0,0.055));
  }
  .brand {
    position: absolute;
    display: flex;
    align-items: center;
    gap: 10px;
    font-weight: 900;
    letter-spacing: 1px;
    text-transform: uppercase;
    white-space: nowrap;
  }
  .brand__mark { display: block; flex: none; }
  .card--front .brand {
    left: 34px;
    top: 120px;
    color: var(--brand-green);
    font-size: 21px;
  }
  .card--front .brand__mark { width: 20px; height: 20px; background: var(--brand-green); }
  .front__divider {
    position: absolute;
    left: 290px;
    top: 58px;
    width: 2px;
    height: 150px;
    background: var(--brand-green);
  }
  .contact {
    position: absolute;
    right: 28px;
    top: 34px;
    text-align: right;
    color: var(--ink);
  }
  .contact__name { font-size: 24px; font-weight: 700; line-height: 1.1; }
  .contact__title { font-size: 12px; color: var(--ink-soft); margin-top: 4px; }
  .contact__phones { margin-top: 46px; font-size: 12px; line-height: 1.6; }
  .contact__line { display: flex; justify-content: flex-end; align-items: center; gap: 6px; }
  .contact__line svg { width: 11px; height: 11px; }
  .contact__email {
    position: absolute;
    right: 28px;
    bottom: 42px;
    font-size: 12px;
    color: var(--ink-soft);
  }
  .front__band {
    position: absolute;
    left: 0;
    bottom: 0;
    width: 540px;
    height: 34px;
  }
  .front__web {
    position: absolute;
    right: 28px;
    bottom: 10px;
    font-size: 12px;
    color: var(--white);
    letter-spacing: 0.3px;
  }
  /* ---------- Back ---------- */
  .card--back {
    left: 620px;
    background: linear-gradient(135deg, var(--card-dark-a) 0%, var(--card-dark-b) 100%);
  }
  .back__pattern {
    position: absolute;
    right: 0;
    top: 0;
    width: 320px;
    height: 150px;
    background: linear-gradient(200deg, rgba(255,255,255,0.06), rgba(255,255,255,0.01));
  }
  .card--back .brand {
    left: 60px;
    top: 178px;
    color: var(--white);
    font-size: 34px;
    gap: 14px;
  }
  .card--back .brand__mark { width: 34px; height: 34px; background: var(--white); }
</style>
</head>
<body>

  <section class="card card--front" aria-label="Business card front">
    <div class="front__watermark" role="img" aria-label="Faint embossed brand emblem"></div>

    <div class="brand">
      <span class="brand__mark"></span>
      <span class="brand__name">Harwell Capital</span>
    </div>

    <div class="front__divider"></div>

    <div class="contact">
      <p class="contact__name">Danica Pruett</p>
      <p class="contact__title">Executive Assistant</p>
      <div class="contact__phones">
        <p class="contact__line">+64 21 547 3162
          <svg viewBox="0 0 12 12" aria-hidden="true"><rect x="3" y="0.5" width="6" height="11" rx="1.2" fill="none" stroke="#232323" stroke-width="1.2"/><rect x="5" y="9.2" width="2" height="1" fill="#232323"/></svg>
        </p>
      </div>
    </div>

    <p class="contact__email">danicap@harwellcapital.co.nz</p>

    <svg class="front__band" viewBox="0 0 540 34" aria-hidden="true">
      <polygon points="0,4 236,4 210,34 0,34" fill="var(--brand-green)"/>
      <polygon points="244,4 254,4 228,34 218,34" fill="var(--band-rule)"/>
      <polygon points="262,4 540,4 540,34 236,34" fill="var(--band-dark)"/>
    </svg>
    <p class="front__web">www.harwellcapital.co.nz</p>
  </section>

  <section class="card card--back" aria-label="Business card back">
    <div class="back__pattern" role="img" aria-label="Subtle embossed repeating brand pattern"></div>
    <div class="brand">
      <span class="brand__mark"></span>
      <span class="brand__name">Harwell Capital</span>
    </div>
  </section>

</body>
</html>
```